Orva Business Card

we need a business card for flooring business called Orva Flooring, the design should be black and white. we have 2 locations

Kellbrook Showroom
527 Kellerman Road,
Kellbrook VIC 3158

Ashmere Showroom
462 Bramwell Hwy,
Ashmere VIC 3217

email : sales@orvaflooring.com.au
(03) 9471 2830

Please inform we sell , Laminate, Hybrid, Timber, carpet and commercial flooring

```html
<!DOCTYPE html>
<html lang="en">
<head>
<meta charset="utf-8">
<title>Orva Flooring Business Card</title>
<link href="https://fonts.googleapis.com/css2?family=Montserrat:wght@300;400;700&display=swap" rel="stylesheet">
<style>
  :root {
    --page-bg: #e9ecf0;
    --card-black: #0d0d0d;
    --card-sheen: #1e1e1e;
    --ink-white: #f2f2f2;
    --ink-soft: #bdbdbd;
    --ink-faint: rgba(255,255,255,0.07);
    --ink-brand: #9a9a9a;
    --band-grey: #a3a3a3;
    --band-ink: #111111;
  }
  * { box-sizing: border-box; margin: 0; padding: 0; }
  html, body { width: 1200px; height: 876px; overflow: hidden; }
  body {
    background: var(--page-bg);
    font-family: "Montserrat", Arial, sans-serif;
    display: flex;
    align-items: center;
    justify-content: center;
    gap: 50px;
  }
  .card {
    position: relative;
    width: 540px;
    height: 309px;
    background: radial-gradient(ellipse at 30% 20%, var(--card-sheen), var(--card-black) 70%);
    color: var(--ink-white);
    overflow: hidden;
    box-shadow: 0 10px 30px rgba(0,0,0,0.25);
  }
  .brand {
    font-weight: 300;
    letter-spacing: 2px;
    text-transform: uppercase;
    color: var(--ink-white);
    white-space: nowrap;
    line-height: 1;
  }
  .brand-watermark {
    position: absolute;
    font-weight: 300;
    letter-spacing: 3px;
    text-transform: uppercase;
    color: var(--ink-faint);
    white-space: nowrap;
    line-height: 1;
  }

  /* Front */
  .card-front .brand { position: absolute; top: 34px; left: 36px; font-size: 22px; }
  .card-front .brand-watermark { right: 36px; bottom: 56px; font-size: 42px; }
  .person { position: absolute; top: 128px; left: 36px; }
  .person-name { font-size: 20px; font-weight: 700; letter-spacing: 1px; line-height: 1.2; }
  .person-name span { font-weight: 400; }
  .person-role { font-size: 11px; color: var(--ink-soft); margin-top: 4px; letter-spacing: 1px; }
  .contact-list {
    position: absolute; right: 36px; top: 120px;
    list-style: none; font-size: 15px; font-weight: 300;
  }
  .contact-list li { display: flex; align-items: center; justify-content: flex-end; gap: 10px; margin-bottom: 12px; line-height: 1.2; }
  .contact-list svg { width: 14px; height: 14px; fill: var(--ink-white); flex: none; }
  .service-band {
    position: absolute; left: 0; right: 0; bottom: 0; height: 36px;
    background: var(--band-grey); color: var(--band-ink);
    display: flex; align-items: center; justify-content: center;
    font-size: 11px; font-weight: 400; letter-spacing: 1.2px; text-transform: uppercase;
  }

  /* Back */
  .card-back .brand { position: absolute; left: 36px; bottom: 40px; font-size: 44px; color: var(--ink-brand); letter-spacing: 4px; }
  .showrooms { position: absolute; top: 32px; right: 36px; text-align: right; font-size: 13px; font-weight: 300; line-height: 1.45; }
  .showroom + .showroom { margin-top: 12px; }
  .showroom-title { display: flex; align-items: center; justify-content: flex-end; gap: 8px; }
  .showroom-title svg { width: 11px; height: 13px; fill: var(--ink-white); flex: none; }
</style>
</head>
<body>

<section class="card card-front">
  <div class="brand">Orva Flooring</div>
  <div class="brand-watermark" aria-hidden="true">Orva Flooring</div>
  <div class="person">
    <div class="person-name">TOMAS<span>REYLAND</span></div>
    <div class="person-role">Director</div>
  </div>
  <ul class="contact-list">
    <li>(03) 9471 2830
      <svg viewBox="0 0 24 24" aria-hidden="true"><path d="M6.6 10.8a15.1 15.1 0 0 0 6.6 6.6l2.2-2.2c.3-.3.7-.4 1-.2 1.1.4 2.3.6 3.6.6.6 0 1 .4 1 1V20c0 .6-.4 1-1 1A17 17 0 0 1 3 4c0-.6.4-1 1-1h3.5c.6 0 1 .4 1 1 0 1.3.2 2.5.6 3.6.1.3 0 .7-.2 1z"/></svg>
    </li>
    <li>sales@orvaflooring.com.au
      <svg viewBox="0 0 24 24" aria-hidden="true"><path d="M2 5h20v14H2zm2 2v.5l8 5 8-5V7z"/></svg>
    </li>
  </ul>
  <div class="service-band">Laminate, Hybrid, Timber, Carpet and Commercial Flooring</div>
</section>

<section class="card card-back">
  <div class="showrooms">
    <div class="showroom">
      <div class="showroom-title">Kellbrook Showroom
        <svg viewBox="0 0 20 24" aria-hidden="true"><path d="M10 0a8 8 0 0 0-8 8c0 6 8 16 8 16s8-10 8-16a8 8 0 0 0-8-8zm0 11a3 3 0 1 1 0-6 3 3 0 0 1 0 6z"/></svg>
      </div>
      <div>527 Kellerman Road,</div>
      <div>Kellbrook VIC 3158</div>
    </div>
    <div class="showroom">
      <div class="showroom-title">Ashmere Showroom</div>
      <div>462 Bramwell Hwy,</div>
      <div>Ashmere VIC 3217</div>
    </div>
  </div>
  <div class="brand">Orva Flooring</div>
</section>

</body>
</html>
```